Design a new product for a successful cannabis company

We need a package design for a new brand. We are a large cannabis company near Seattle, USA. The name of the product is called the "Velmora Quill". It is a pure cannabis oil extract that is used through a magnetic vaporizer cartridge. We need a graphic template designed that will be printed on a card and inserted into the plastic packaging. This project is design the overall concept, and we will add the required warnings on our end once a design is chosen.

Dimensions:
Width - 2.5625 inches
Height - 3.3125 inches
Viewing Window Width - .4375 inches
Viewing Window Height - 2.0 Inches
Distance from the bottom of the card to the viewing window- .4375 inches
Distance from the left side to the viewing window - 1.0625 inch
Distance from the right side to the viewing window - 1.0625 inch

Theme:
- We would like it to have some sort of Velmora Quill historical feel. I attached the dimensions for size reference. Please extract that "VelmoraQuill" text/font if possible. We really want to use that.
- You could use an old map from that region and time in history.
- Wiki link explaining the Velmora Quill (https://en.lorevault.example/wiki/Velmora_Quill)

Additional Notes:
- There is an area where the physical cartridge will go. Feel free to extend the background into that area but please do not place any text there.
- There is a backside of this package that customers will see. We will place our warning text back there along with a product description. Please keep the back side clear of text but have it match whatever color scheme or background you do on the front side.
- I included an example of a competitor using the same package shape. That's what it will be printed on

Please reach out if you have questions or need clarification. I will be adding details as we go to help with the concept. Thank you!

Target Market(s)

Cannabis oil users of all ages

Colors

Designer to choose colors to be used in the design.

Requirements
Must have
• The same VelmoraQuill text from the attached concert poster
• Must say "A magnetic vape cartridge."
Nice to have
• A historical feel by faintly using an 12th century English map as the background. Open to anything in order to achieve a classic feel.
Should not have
• Bright colors

```html
<!DOCTYPE html>
<html lang="en">
<head>
<meta charset="utf-8">
<title>Velmora Quill – Cartridge Card</title>
<link rel="stylesheet" href="https://fonts.googleapis.com/css2?family=Righteous&family=Josefin+Sans:wght@300;600&display=swap">
<style>
  :root {
    --page: #ffffff;
    --parchment-light: #efe2c2;
    --parchment-mid: #d9c197;
    --parchment-dark: #a88455;
    --ink-edge: #3a2a1c;
    --oxblood: #6e0f12;
    --seal-dark: #5a4534;
    --seal-mid: #7a6350;
    --label-bg: #d8cbb2;
    --label-ink: #3b2a20;
    --text-dark: #1e1712;
    --text-light: #fbf6ec;
  }
  * { box-sizing: border-box; margin: 0; padding: 0; }
  html, body {
    width: 1094px; height: 1200px; overflow: hidden;
    background: var(--page);
  }
  .canvas { position: relative; width: 1094px; height: 1200px; }

  .card {
    position: absolute; left: 290px; top: 262px;
    width: 502px; height: 654px;
    border-radius: 24px;
    border: 1.5px solid var(--ink-edge);
    overflow: hidden;
  }
  .card__map {
    position: absolute; inset: 0;
    background:
      radial-gradient(ellipse at 62% 40%, rgba(255,250,230,0.75), transparent 55%),
      radial-gradient(ellipse at 20% 80%, rgba(120,85,50,0.35), transparent 60%),
      radial-gradient(ellipse at 90% 15%, rgba(110,80,50,0.35), transparent 45%),
      linear-gradient(160deg, var(--parchment-mid), var(--parchment-light) 45%, var(--parchment-mid) 75%, var(--parchment-dark));
  }

  .card__window {
    position: absolute; left: 60px; top: 60px;
    width: 82px; height: 556px;
    border: 1.2px solid var(--ink-edge);
    border-radius: 12px;
  }

  .card__title {
    position: absolute; left: 160px; top: 76px; width: 330px;
    font-family: "Righteous", sans-serif;
    color: var(--oxblood);
    font-size: 70px; line-height: 80px;
    letter-spacing: -3px;
    text-transform: uppercase;
  }

  .seal {
    position: absolute; left: 203px; top: 252px;
    width: 236px; height: 236px;
  }
  .seal__disc {
    position: absolute; inset: 0; border-radius: 50%;
    background: radial-gradient(circle at 50% 45%, var(--seal-mid), var(--seal-dark) 75%);
    box-shadow: 0 0 14px rgba(255,248,230,0.9);
  }
  .seal__label {
    position: absolute; left: 48px; top: 72px;
    width: 140px; height: 92px;
    background: var(--label-bg);
    border: 1.5px solid var(--label-ink);
    border-radius: 8px;
    display: flex; flex-direction: column; justify-content: center; align-items: center;
    font-family: "Josefin Sans", sans-serif; font-weight: 300;
    font-size: 17px; line-height: 22px;
    color: var(--label-ink); text-transform: uppercase; text-align: center;
    letter-spacing: -0.5px;
  }

  .card__maker {
    position: absolute; left: 164px; top: 516px; width: 320px;
    font-family: "Josefin Sans", sans-serif; font-weight: 300;
    font-size: 25px; letter-spacing: -0.5px;
    color: var(--text-dark); text-transform: uppercase; text-align: center;
  }
  .card__compat {
    position: absolute; left: 164px; top: 586px; width: 320px;
    font-family: "Josefin Sans", sans-serif; font-weight: 600;
    font-size: 13px; letter-spacing: -0.2px;
    color: var(--text-light); text-transform: uppercase; text-align: center;
    text-shadow: 0 0 3px rgba(40,25,15,0.95), 0 0 6px rgba(40,25,15,0.8);
  }
</style>
</head>
<body>
<div class="canvas">
  <section class="card">
    <div class="card__map" role="img" aria-label="Antique parchment map of the British Isles with coastlines, place names and a compass rose"></div>
    <div class="card__window" aria-hidden="true"></div>

    <h1 class="card__title">Velmora<br>Quill</h1>

    <div class="seal">
      <div class="seal__disc" role="img" aria-label="Round seal with ornate floral scrollwork"></div>
      <div class="seal__label">A Magnetic<br>Vape<br>Cartridge™</div>
    </div>

    <p class="card__maker">A Harborwend Product</p>
    <p class="card__compat">For use with most magnetic batteries</p>
  </section>
</div>
</body>
</html>
```